依頼詳細
◆ディナーショー詳細

・鳴瀬野ガーデンホテル(かつて天皇陛下も宿泊された、格式&レトロ感のあるホテル)にて開催。ディナーはフランス料理
・ショー第1部:二胡と箏(着物ドレス着用)(和風の音楽でスタート)
第2部:二胡とピアノ(カクテルドレス)
(生命の息吹を感じる季節・コロナも明けて・自身の九死に一生を得た体験を含めて、生きる歓びを語るようなトークを交えて)
第3部:二胡とソノリカ(トレーンの長いゴージャスなドレス)
(プロジェクターを使用し、画像や動画で世界観を演出)
・紅茶コンサルタントが、コース一品ずつに合わせ、料理に合う紅茶を提供
・ホテル本館2階ラウンジからは、海に浮かぶ「竹島」の絶景が眺められる。
17時よりラウンジにて、夕陽に染まる絶景を見ながらウェルカムドリンクを嗜んでいただく。
宴会場へ移動し、18時よりショースタート。
・桜の咲く時期を選んで開催

◆デザイン要望

・上記のディナーショーがイメージできるようなデザイン
もしくは
チラシを一枚見るだけで「どんなショーなのだろう?」とディナーショーへ期待の膨らむようなデザイン
(・・・でありながら、主役がぼけないチラシ)が希望です。
記載項目
掲載内容のテキストは、添付のエクセルファイルをご参照ください。ページ内に、宣材写真のダウンロードURLも貼ってありますので、写真はそこからご使用ください。(写真の使用枚数等こだわりはありません)
サイズ
A4
ページ数
片面
希望イメージ
シンプル 複雑
単色 カラフル
暗い 明るい
日常 高級
遊び心 厳粛
未来的 伝統的
女性的 男性的
希望する色
設定なし
納品ファイル
• 高解像度JPG (.jpg)
• PNG形式 (.png)
補足説明
・もし可能でしたら、印刷(コピエールやモナリト等)入稿まで行っていただくか、入稿方法をご指南いただけると助かります。印刷費用については、別途予算を組んでおります。
・今回依頼が初めてで不慣れな点が多々あります。ご不明な点やご指摘等ありましたら、仰っていただけますようよろしくお願いいたします。
■ 選んだ理由

素敵な作品を沢山ご提案いただき、私としては絞りきれず、とても迷ってしまいました。そこで、家族やディナーショーの協力者、スタッフなど、複数の方に相談したところ、多数決で柚木様のデザインに票が集まり、決定させていただきました。全体的に優しい色味で文字も見やすく、気に入っています。

■ 提案者全員のお礼・コメント

この度は沢山のご提案をいただき、本当にありがとうございました。ご提案をいただく度に、A4用紙一枚に込められたデザインの多様性やデザイナーさんの思い、一瞬にしてインパクトを与えるチラシデザインの奥深さに感動して、何度か目が潤んでしまいました。できれば部屋に飾っておきたい作品もありましたが、そういう選択ができないのが残念です。また依頼させていただく際には、よろしくお願い致します。

```html
<!DOCTYPE html>
<html lang="ja">
<head>
<meta charset="utf-8">
<title>篠宮玲花 スプリングディナーショー</title>
<link href="https://fonts.googleapis.com/css2?family=Shippori+Mincho+B1:wght@400;600;800&family=Great+Vibes&family=Noto+Sans+JP:wght@400;500;700&display=swap" rel="stylesheet">
<style>
  :root{
    --pink:#e46a93;
    --pink-deep:#d4517f;
    --pink-soft:#f3c3d2;
    --blush:#fbe4ec;
    --text:#4a3a40;
    --muted:#7d6b71;
    --white:#ffffff;
    --gold:#b49a6a;
  }
  *{margin:0;padding:0;box-sizing:border-box}
  html,body{width:851px;height:1200px;overflow:hidden;background:var(--white)}
  .flyer{position:relative;width:851px;height:1200px;overflow:hidden;
    font-family:"Shippori Mincho B1",serif;color:var(--text);
    background:linear-gradient(180deg,#fff 0%,#fff6f9 70%,#fde7ee 100%)}

  .hero{position:absolute;left:0;top:0;width:851px;height:770px;
    background:linear-gradient(160deg,#f0aac0 0%,#f8d3de 35%,#fbe4ea 60%,#f4bfcf 100%)}
  .hero-photo{position:absolute;left:270px;top:0;width:390px;height:770px;
    background:radial-gradient(ellipse at 50% 45%,#fff8f4 0%,#f3dcd8 45%,rgba(246,198,212,0) 75%)}
  .hero-fade{position:absolute;left:0;top:690px;width:851px;height:80px;
    background:linear-gradient(180deg,rgba(255,255,255,0),#fff)}

  .tagline{position:absolute;left:110px;top:40px;height:220px;writing-mode:vertical-rl;
    color:var(--white);font-size:20px;line-height:1.75;letter-spacing:.12em;font-weight:600;
    text-shadow:0 0 6px rgba(200,90,130,.5)}

  .title{position:absolute;writing-mode:vertical-rl;color:var(--pink-deep);font-weight:800;white-space:nowrap}
  .title-role{right:46px;top:28px;font-size:30px;letter-spacing:.08em}
  .title-name{right:100px;top:34px;font-size:72px;letter-spacing:.04em;line-height:1}
  .title-show{right:190px;top:95px;font-size:29px;letter-spacing:.02em;line-height:1}
  .script{position:absolute;right:238px;top:110px;writing-mode:vertical-rl;white-space:nowrap;
    font-family:"Great Vibes",cursive;color:var(--white);font-size:27px;line-height:1.1;
    text-shadow:0 0 4px rgba(212,81,127,.6)}

  .profile{position:absolute;left:14px;top:625px;width:160px;padding:7px 9px;
    background:rgba(255,255,255,.55);border-radius:4px;font-family:"Noto Sans JP",sans-serif;
    font-size:8px;line-height:1.55;color:var(--muted)}
  .profile b{display:block;font-family:"Great Vibes",cursive;font-size:14px;color:var(--pink);font-weight:400}

  .date{position:absolute;right:24px;top:668px;color:var(--pink-deep);font-weight:800;white-space:nowrap;line-height:1}
  .date .y{font-size:28px}
  .date .md{font-size:64px}
  .date .unit{font-size:30px}
  .date .dow{display:inline-block;width:46px;height:46px;border-radius:50%;background:var(--pink);
    color:var(--white);font-size:17px;line-height:46px;text-align:center;vertical-align:middle;margin-left:4px}

  .gallery{position:absolute;left:14px;top:772px;display:flex;gap:10px}
  .gallery div{width:198px;height:92px;border-radius:3px}
  .g-hotel{background:linear-gradient(180deg,#bcd3e8,#8fa88a)}
  .g-hall{background:linear-gradient(180deg,#2c2656,#7b4c8e)}
  .g-dinner{background:linear-gradient(180deg,#e9d8b8,#c6a27a)}
  .g-stage{background:linear-gradient(180deg,#f3e3e6,#c98aa0)}

  .venue{position:absolute;left:0;top:876px;width:851px;text-align:center}
  .venue-name{display:inline-flex;align-items:center;gap:14px;font-size:44px;font-weight:800;color:var(--text);letter-spacing:.06em;line-height:1.2}
  .venue-mark{width:30px;height:30px;border-radius:50%;background:var(--gold)}
  .venue-addr{font-family:"Noto Sans JP",sans-serif;font-size:11px;color:var(--muted);margin-top:4px;letter-spacing:.05em}

  .schedule{position:absolute;left:24px;top:978px;width:520px}
  .slot{margin-bottom:8px}
  .slot-head{font-size:15px;font-weight:700;display:flex;gap:14px}
  .slot-head .time{color:var(--pink-deep)}
  .slot p{font-family:"Noto Sans JP",sans-serif;font-size:9.5px;color:var(--muted);line-height:1.5;margin-top:2px}

  .program{position:absolute;right:26px;top:980px;width:230px;list-style:none}
  .program li{font-size:16px;font-weight:700;margin-bottom:8px;display:flex;gap:10px;align-items:center}
  .program .part{color:var(--white);background:var(--pink);padding:0 7px;font-size:14px;border-radius:3px}

  .price{position:absolute;left:24px;top:1068px;display:flex;align-items:baseline;gap:10px}
  .price .lbl{font-size:15px;font-weight:600}
  .price .amt{font-size:44px;font-weight:800;color:var(--pink-deep);line-height:1}
  .price .tax{font-family:"Noto Sans JP",sans-serif;font-size:10px;color:var(--muted)}

  .contact-mail{position:absolute;left:470px;top:1070px;font-family:"Noto Sans JP",sans-serif}
  .contact-mail .k{font-size:12px;font-weight:500}
  .contact-mail .v{font-size:16px;font-weight:700;color:var(--pink-deep)}

  .footer{position:absolute;left:0;top:1128px;width:851px;height:72px;background:var(--blush);
    display:flex;justify-content:space-between;align-items:center;padding:0 24px}
  .link{font-family:"Noto Sans JP",sans-serif}
  .link .k{font-size:13px;font-weight:700;color:var(--text)}
  .link .v{font-size:13px;color:var(--pink-deep);margin-top:4px}
</style>
</head>
<body>
<main class="flyer">
  <section class="hero">
    <div class="hero-photo" role="img" aria-label="二胡を構えて微笑む白いドレスの奏者と桜並木の写真"></div>
    <div class="hero-fade"></div>
    <p class="tagline">偉大の師を継ぐ<br>二胡の調べが<br>あなたを<br>別世界へ誘います</p>
    <h1>
      <span class="title title-role">二胡奏者</span>
      <span class="title title-name">篠宮玲花</span>
      <span class="title title-show">スプリングディナーショー</span>
    </h1>
    <p class="script">Reika Shinomiya Spring Dinner Show</p>
    <div class="profile"><b>Profile</b>幼少より二胡に親しみ、名師に師事。国内外の舞台で演奏を重ね、心に寄り添う音色で多くの聴衆を魅了している。</div>
    <p class="date"><span class="y">2023年</span><span class="md">4</span><span class="unit">月</span><span class="md">3</span><span class="unit">日</span><span class="dow">sun</span></p>
  </section>

  <div class="gallery">
    <div class="g-hotel" role="img" aria-label="レトロなホテル外観の写真"></div>
    <div class="g-hall" role="img" aria-label="シャンデリアの宴会場の写真"></div>
    <div class="g-dinner" role="img" aria-label="フランス料理のテーブルの写真"></div>
    <div class="g-stage" role="img" aria-label="二胡を演奏する奏者の写真"></div>
  </div>

  <div class="venue">
    <div class="venue-name"><span class="venue-mark"></span>鳴瀬野ガーデンホテル</div>
    <p class="venue-addr">〒400-0000 架空県鳴瀬野市浜風町1-1　TEL.0000-00-0000</p>
  </div>

  <div class="schedule">
    <div class="slot">
      <div class="slot-head"><span>ウェルカムドリンク</span><span class="time">17:00～</span><span>本館メインダイニングルーム</span></div>
      <p>紅茶コンサルタント Sayo Minase 氏のウェルカムティーをお楽しみ下さい</p>
    </div>
    <div class="slot">
      <div class="slot-head"><span>ショー&amp;ディナー</span><span class="time">18:00～</span><span>別館バンケットホール</span></div>
      <p>美味しいお料理と音色を共に、特別なひと時をお過ごし下さい</p>
    </div>
  </div>

  <ul class="program">
    <li><span class="part">第一部</span>二胡と箏</li>
    <li><span class="part">第二部</span>二胡とピアノ</li>
    <li><span class="part">第三部</span>二胡とソノリカ</li>
  </ul>

  <div class="price"><span class="lbl">お一人様</span><span class="amt">¥27,000</span><span class="tax">(税・サービス料込)</span></div>
  <div class="contact-mail"><p class="k">ご予約・お問い合わせアドレス</p><p class="v">niko@reika-shinomiya.example</p></div>

  <footer class="footer">
    <div class="link"><p class="k">篠宮玲花オフィシャルサイト</p><p class="v">www.reika-shinomiya.example</p></div>
    <div class="link"><p class="k">ご予約フォーム</p><p class="v">www.reika-shinomiya.example/contact</p></div>
  </footer>
</main>
</body>
</html>
```